Business Card Design Project

I want my business cards to stand and feel timeless! I also want people to get their hands on them and freak out over how cool these are, I already have a logo i just want a very cool card design! this is for a makeup artist and maybe one day a line of cosmetics.

Target Market(s)

I want this to target women from 18 to 45

Industry/Entity Type

Business

Font styles to use
Decorative
Script

Colors

Designer to choose colors to be used in the design.

Requirements
Must have
• it must be elegante

```html
<!DOCTYPE html>
<html lang="en">
<head>
<meta charset="utf-8">
<title>Clara Joy — Make Up Artist Business Card</title>
<link rel="stylesheet" href="https://fonts.googleapis.com/css2?family=Pinyon+Script&family=Quicksand:wght@300;400&display=swap">
<style>
  :root {
    --backdrop: #e4e4e6;
    --card-white: #ffffff;
    --card-navy: #131c2e;
    --ink-navy: #1a2236;
    --ink-muted: #6f7890;
    --ink-body: #3a3f4c;
    --hair-dark: #0d1426;
    --hair-blue: #3f6bb0;
    --hair-light: #c9d6ea;
    --rule: #5d6780;
    --ink-light: #f4f5f8;
  }
  * { margin: 0; padding: 0; box-sizing: border-box; }
  html, body {
    width: 1200px;
    height: 1200px;
    overflow: hidden;
    background: var(--backdrop);
  }
  .canvas {
    position: relative;
    width: 1200px;
    height: 1200px;
  }
  .card {
    position: absolute;
    left: 253px;
    width: 678px;
    height: 376px;
    overflow: hidden;
  }
  .card--front {
    top: 168px;
    background: var(--card-white);
  }
  .card--back {
    top: 656px;
    background: var(--card-navy);
  }
  .portrait-area {
    position: absolute;
    left: 0;
    top: 0;
    width: 440px;
    height: 376px;
    background: linear-gradient(100deg, var(--hair-dark) 0%, var(--hair-dark) 22%, var(--hair-blue) 55%, var(--hair-light) 78%, var(--card-white) 100%);
  }
  .front-details {
    position: absolute;
    left: 336px;
    width: 320px;
    top: 52px;
    text-align: center;
    font-family: "Quicksand", sans-serif;
  }
  .front-name {
    font-family: "Pinyon Script", cursive;
    font-weight: 400;
    font-size: 50px;
    line-height: 1.1;
    color: var(--ink-navy);
  }
  .front-role {
    font-size: 17px;
    letter-spacing: 0.5px;
    color: var(--ink-muted);
    margin-top: -2px;
  }
  .front-contact {
    margin-top: 40px;
    font-size: 20px;
    line-height: 34px;
    letter-spacing: 0.6px;
    color: var(--ink-body);
    list-style: none;
  }
  .back-name {
    position: absolute;
    left: 0;
    right: 0;
    top: 118px;
    text-align: center;
    font-family: "Quicksand", sans-serif;
    font-weight: 300;
    font-size: 56px;
    letter-spacing: 6px;
    color: var(--ink-light);
  }
  .back-rule {
    position: absolute;
    left: 78px;
    width: 520px;
    top: 224px;
    height: 1px;
    background: var(--rule);
  }
  .back-web {
    position: absolute;
    left: 0;
    right: 0;
    top: 258px;
    text-align: center;
    font-family: "Quicksand", sans-serif;
    font-weight: 400;
    font-size: 26px;
    letter-spacing: 1.4px;
    color: var(--ink-light);
  }
</style>
</head>
<body>
<main class="canvas">
  <section class="card card--front">
    <div class="portrait-area" role="img" aria-label="Illustration of a woman with long flowing dark and blue wavy hair"></div>
    <div class="front-details">
      <h1 class="front-name">Clara Joy</h1>
      <p class="front-role">Make Up Artist</p>
      <ul class="front-contact">
        <li>555014-7720</li>
        <li>hello@clarajoy.com</li>
      </ul>
    </div>
  </section>

  <section class="card card--back">
    <p class="back-name">CLARA JOY</p>
    <div class="back-rule"></div>
    <p class="back-web">www.clarajoymakeup.com</p>
  </section>
</main>
</body>
</html>
```